Design a Unique and Eye-Catching Necklace Card for Verandelle's New Lumenwave Line

Attention all creative minds from around the world! Verandelle, a company known for its free-spirited and bohemian chic vibe, is proud to announce a new design contest. We are inviting you to create a dynamic and unique necklace card for our upcoming Lumenwave line.

Our new Lumenwave line comprises 12-20 unique necklace combinations. Each necklace features different stones, each with its own healing properties and associated zodiac sign. We are looking for a template that can be easily modified to change the names of the stones, zodiac sign, and the colors to match the specific stones on each necklace.

The card should be 3 x 4,
It should include the names of the stones, the associated zodiac sign (if applicable), a few words about the healing properties of the stones, and a captivating graphic that represents the colors of the stones.

Our goal is to delight our customers with packaging as unique as the necklaces themselves. The necklace should be the focal point, but the text and graphic on the card should also draw the eye.

Please note that our target audience includes mid-priced boutiques across the country and festival-goers in Colorado. Your design should reflect the unique taste and free spirit of our clientele.

We are excited to see your creativity shine in this project. If there are any points that need clarification, please do not hesitate to ask. We look forward to your participation in bringing the Lumenwave line to life!
https://www.plorvex.example/board/QKTm_ZRwpe/u3hb9XKdLqWm72RtPoaVnc/edit?ref=QKTm_ZRwpe&src=share

https://www.plorvex.example/board/QKTr_BNyhwa/t8Ld-WsPzMEY246VqoXjNd/edit?ref=QKTr_BNyhwa&src=share
I want to use the flowing watercolor and have it change with each necklace color.
Use the necklaces below. Incorporate the zodiac symbol as is shown below.

Examples of other cards in our collection

The Little Pebble Pendant: https://www.plorvex.example/board/QKTh_WomRtc/pbMRx63CKqnYs905Bd-aLe/edit?ref=QKTh_WomRtc&src=share

Other examples of necklace cards I like:

https://www.tindramart.example/item/731920584/green-emerald-stone-necklace-emerald?k=a1b2c3d4e5f60718293a4b5c6d7e8f9012345678&s=7d3e91ab

https://www.tindramart.example/item/846201937/january-birthstone-necklace-green-garnet?k=b2c3d4e5f60718293a4b5c6d7e8f901234567890&s=4c82fe10

https://www.tindramart.example/item/2093748165/natural-crystal-bracelets-empath?k=c3d4e5f60718293a4b5c6d7e8f90123456789012&s=9ab0c37d

https://www.tindramart.example/item/2174603958/black-obsidian-protection-necklace-black?k=d4e5f60718293a4b5c6d7e8f9012345678901234&s=e15d6b28

Target Market(s)

Women aged 25-50 with a spiritual, hippy, bohemain, yoga vibe.

Industry/Entity Type

Handmade Jewelry | Wholesale jewelry | Retail Jewelry sales at Festivals

Font styles to use
Script

Colors

Designer to choose colors to be used in the design.

Requirements
Must have
• A template that can be interchangable with the stone colors, names and healing properties.
Nice to have
• Some different ideas about the graphic color patterns on the card.
Should not have
• Any graphic that would cover the middle of the necklace card and keep people from seeing the neckalce

```html
<!DOCTYPE html>
<html lang="en">
<head>
<meta charset="utf-8">
<title>Sagittarius Turqouise Necklace Card</title>
<link rel="stylesheet" href="https://fonts.googleapis.com/css2?family=Fira+Sans:wght@300;400&display=swap">
<style>
  :root {
    --backdrop: #dcebeb;
    --card: #ffffff;
    --petal-deep: #2f7f80;
    --petal-mid: #5d9fa0;
    --wash: #d6e8e8;
    --sign-blue: #5b7fd0;
    --stone-tint: #cfe3e4;
    --tag-blue: #6e8fd6;
    --gold-line: #d9b49a;
    --chain: #8a7d74;
    --bead-brown: #7a3f22;
    --bead-teal: #2f8a84;
    --bead-sky: #3fb0c8;
  }
  * { margin: 0; padding: 0; box-sizing: border-box; }
  html, body {
    width: 1200px; height: 1200px; overflow: hidden;
    background: var(--backdrop);
  }
  .necklace-card {
    position: absolute;
    left: 195px; top: 60px;
    width: 810px; height: 1080px;
    background: var(--card);
    border-radius: 26px;
    overflow: hidden;
  }
  .card-art { position: absolute; inset: 0; width: 100%; height: 100%; }
  .zodiac-sign, .stone-name, .healing-note {
    position: absolute; left: 0; width: 100%;
    text-align: center;
    font-family: "Fira Sans", sans-serif;
    white-space: nowrap;
  }
  .zodiac-sign {
    top: 290px;
    font-size: 42px; font-weight: 400;
    letter-spacing: 5px;
    color: var(--sign-blue);
  }
  .stone-name {
    top: 345px;
    font-size: 80px; font-weight: 300;
    letter-spacing: 7px;
    text-indent: 7px;
    color: var(--stone-tint);
  }
  .healing-note {
    top: 838px;
    font-size: 22px; font-weight: 400;
    letter-spacing: 5px;
    text-indent: 5px;
    color: var(--tag-blue);
  }
</style>
</head>
<body>
  <div class="necklace-card">
    <svg class="card-art" viewBox="0 0 810 1080" xmlns="http://www.w3.org/2000/svg">
      <defs>
        <radialGradient id="petalTop" cx="0" cy="0" r="1" gradientUnits="objectBoundingBox">
          <stop offset="0" stop-color="var(--petal-deep)"/>
          <stop offset="0.55" stop-color="var(--petal-mid)" stop-opacity="0.85"/>
          <stop offset="1" stop-color="var(--petal-mid)" stop-opacity="0"/>
        </radialGradient>
        <radialGradient id="petalBottom" cx="1" cy="1" r="1" gradientUnits="objectBoundingBox">
          <stop offset="0" stop-color="var(--petal-deep)"/>
          <stop offset="0.55" stop-color="var(--petal-mid)" stop-opacity="0.85"/>
          <stop offset="1" stop-color="var(--petal-mid)" stop-opacity="0"/>
        </radialGradient>
        <radialGradient id="washTop" cx="0.6" cy="0" r="0.8">
          <stop offset="0" stop-color="var(--wash)"/>
          <stop offset="1" stop-color="var(--wash)" stop-opacity="0"/>
        </radialGradient>
        <radialGradient id="washBottom" cx="0.2" cy="1" r="0.8">
          <stop offset="0" stop-color="var(--wash)"/>
          <stop offset="1" stop-color="var(--wash)" stop-opacity="0"/>
        </radialGradient>
        <radialGradient id="starGlow" cx="0.5" cy="0.5" r="0.5">
          <stop offset="0" stop-color="var(--gold-line)" stop-opacity="0.3"/>
          <stop offset="1" stop-color="var(--gold-line)" stop-opacity="0"/>
        </radialGradient>
        <linearGradient id="beadRow" x1="0" y1="0" x2="1" y2="0">
          <stop offset="0" stop-color="var(--bead-brown)"/>
          <stop offset="0.15" stop-color="var(--bead-brown)"/>
          <stop offset="0.3" stop-color="var(--bead-teal)"/>
          <stop offset="0.4" stop-color="var(--bead-sky)"/>
          <stop offset="0.6" stop-color="var(--bead-teal)"/>
          <stop offset="0.85" stop-color="var(--bead-teal)"/>
          <stop offset="1" stop-color="var(--bead-brown)"/>
        </linearGradient>
      </defs>

      <rect class="wash-top" x="250" y="0" width="560" height="220" fill="url(#washTop)"/>
      <rect class="wash-bottom" x="0" y="840" width="560" height="240" fill="url(#washBottom)"/>

      <rect class="petals-top" role="img" aria-label="Watercolor teal petals blooming from the top left corner"
            x="0" y="0" width="410" height="380" fill="url(#petalTop)"/>
      <rect class="petals-bottom" role="img" aria-label="Watercolor teal petals blooming from the bottom right corner"
            x="450" y="700" width="360" height="380" fill="url(#petalBottom)"/>

      <ellipse class="constellation" role="img" aria-label="Sagittarius constellation drawn in gold star lines"
               cx="420" cy="571" rx="128" ry="128" fill="url(#starGlow)"/>

      <g class="necklace-chain" stroke="var(--chain)" stroke-width="1.6" fill="none">
        <path d="M22 12 L212 585"/>
        <path d="M797 16 L612 585"/>
      </g>
      <path class="necklace-beads" role="img" aria-label="Faceted turquoise and brown gemstone beads strung along the chain"
            d="M200 580 C240 700 300 790 405 800 C510 790 575 700 625 580 L603 575 C560 680 500 765 405 772 C310 765 255 680 222 575 Z"
            fill="url(#beadRow)"/>
    </svg>

    <p class="zodiac-sign">Sagittarius</p>
    <p class="stone-name">Turqouise</p>
    <p class="healing-note">PROMORES CONFIDENCE</p>
  </div>
</body>
</html>
```